International Perfume distribution Company needs a stationary design

We are a perfume development and distribution company named GLINTO and based in Sao Paulo Brazil. Basically we licence brazilian and international brands and celebrities to develop and distribute its fragrances and perfumes in Brazil. Our current licenced brands are: Varn Colter, Ravena, Delmor Viqueta fragrances and Lara Monteiro (brazilian soap opera celebrity).

We already have our logo and brand that reflects our massive distribution power in Brazil ("spraying our products accross Brazil") and we are also a branch of a big distribution company named BROMAX. It would be nice to mention it in our stationary ("uma divisao do grupo Bromax").

Industry/Entity Type

It Company

Requirements
Must have
• mention that Glinto is a division/branch of bromax using the following phrase: "uma divisão do grupo Bromax"

Use the logo signature: international fragrances

```html
<!DOCTYPE html>
<html lang="pt">
<head>
<meta charset="utf-8">
<title>Glinto – Business Card</title>
<link href="https://fonts.googleapis.com/css2?family=Quicksand:wght@400;500&family=Arimo:wght@400;700&family=Open+Sans:wght@400&display=swap" rel="stylesheet">
<style>
  :root {
    --brand-purple: #3b2f8c;
    --brand-orange: #f2a21c;
    --card-white: #ffffff;
    --ink: #1e1e24;
    --backdrop: #ece8e3;
  }
  * { margin: 0; padding: 0; box-sizing: border-box; }
  html, body { width: 1200px; height: 806px; overflow: hidden; }
  body {
    background: var(--backdrop);
    position: relative;
    font-family: "Arimo", Arial, sans-serif;
  }
  .card {
    position: absolute;
    width: 540px;
    height: 310px;
    overflow: hidden;
    box-shadow: 0 10px 24px rgba(0,0,0,.18);
  }

  /* Front */
  .card-front { left: 40px; top: 190px; background: var(--card-white); }
  .front-band {
    position: absolute; left: 0; top: 0; bottom: 0; width: 96px;
    background: var(--brand-purple);
  }
  .brand-lockup { position: absolute; left: 78px; top: 38px; display: flex; align-items: center; gap: 22px; }
  .brand-dot {
    width: 76px; height: 76px; border-radius: 50%;
    background: var(--brand-orange); flex: none;
  }
  .brand-text { color: var(--brand-purple); font-family: "Quicksand", Arial, sans-serif; }
  .brand-name { font-size: 60px; font-weight: 400; letter-spacing: 2px; line-height: 1; }
  .brand-signature { font-size: 15px; font-weight: 500; margin-top: 4px; margin-left: 8px; }

  .holder {
    position: absolute; left: 120px; top: 158px;
    padding-bottom: 3px; border-bottom: 2px solid var(--brand-purple);
  }
  .holder-name { color: var(--brand-purple); font-weight: 700; font-size: 21px; }
  .holder-title { color: var(--brand-orange); font-size: 15px; }

  .contact-list { position: absolute; left: 120px; top: 200px; list-style: none; color: var(--ink); font-size: 14px; }
  .contact-list li { display: flex; align-items: center; gap: 7px; height: 21px; }
  .contact-list li.address { margin-top: 7px; }
  .contact-icon { width: 12px; height: 12px; flex: none; }

  /* Back */
  .card-back { left: 620px; top: 300px; background: var(--brand-purple); color: var(--card-white); }
  .back-lockup { position: absolute; left: 0; right: 0; top: 46px; display: flex; justify-content: center; align-items: center; gap: 18px; }
  .back-dot { width: 90px; height: 90px; border-radius: 50%; background: var(--card-white); }
  .back-name { font-family: "Quicksand", Arial, sans-serif; font-size: 46px; font-weight: 400; letter-spacing: 2px; }
  .back-tagline {
    position: absolute; left: 0; right: 0; top: 206px; text-align: center;
    font-family: "Open Sans", Arial, sans-serif; font-size: 17px; letter-spacing: 2px;
  }
  .back-url {
    position: absolute; left: 0; right: 0; top: 248px; text-align: center;
    font-family: "Open Sans", Arial, sans-serif; font-size: 15px; letter-spacing: 4px;
  }
</style>
</head>
<body>

<section class="card card-front">
  <div class="front-band"></div>
  <div class="brand-lockup">
    <div class="brand-dot"></div>
    <div class="brand-text">
      <div class="brand-name">GLINTO</div>
      <div class="brand-signature">international fragrances</div>
    </div>
  </div>

  <div class="holder">
    <span class="holder-name">Your Name,</span>
    <span class="holder-title">Title</span>
  </div>

  <ul class="contact-list">
    <li>
      <svg class="contact-icon" viewBox="0 0 12 12"><circle cx="6" cy="6" r="5.5" fill="none" stroke="#f2a21c" stroke-width="1.2"/><path d="M4 3.5 L5.3 3.5 L5.8 5 L5 5.6 Q5.8 7 7 7.4 L7.6 6.6 L9 7.1 L9 8.3 Q5 8.6 4 3.5Z" fill="#f2a21c"/></svg>
      0987 654321
    </li>
    <li>
      <svg class="contact-icon" viewBox="0 0 12 12"><rect x="3.5" y="1" width="5" height="10" rx="1" fill="#f2a21c"/><rect x="4.4" y="2.2" width="3.2" height="6" fill="#fff"/></svg>
      0987 654321
    </li>
    <li>
      <svg class="contact-icon" viewBox="0 0 12 12"><rect x="1" y="2.5" width="10" height="7" rx="1" fill="#f2a21c"/><path d="M1.5 3 L6 6.5 L10.5 3" fill="none" stroke="#fff" stroke-width="1"/></svg>
      info@glinto.com
    </li>
    <li class="address">
      <svg class="contact-icon" viewBox="0 0 12 12"><circle cx="6" cy="6" r="5.5" fill="#f2a21c"/><path d="M6 2.8 a2 2 0 0 1 2 2 c0 1.5 -2 4 -2 4 s-2 -2.5 -2 -4 a2 2 0 0 1 2 -2z" fill="#fff"/></svg>
      00, Complex name, City, State 0042
    </li>
  </ul>
</section>

<section class="card card-back">
  <div class="back-lockup">
    <div class="back-dot"></div>
    <div class="back-name">GLINTO</div>
  </div>
  <p class="back-tagline">Uma Divisão Do Grupo Bromax</p>
  <p class="back-url">www.glinto.com</p>
</section>

</body>
</html>
```